Business Cards Needed for Innovative Healthcare Marketing Company

We are a marketing company focused on healthcare. Our company is all about rebranding yourself renewing your image and generating results. The phoenix stands for "reborn" or "rising" which we provide new brands for our clients we take their old brands and renew it with creativity and innovation. I am looking for a business card with color dimension. I have attached an example of a card I think has the look and feel of what I am trying to accomplish. I like that the card example has black and grey font colors, I like the font placement and the small logo, I really like the use of the colors on the right those are the colors of my logo. My logo is phoenix so maybe incorporating flames similar to that design. I would like the back a solid color maybe red with an opaque version of the logo and website. As a marketing company I am always open to creative liberty!

Target Market(s)

Doctors and business professionals.

Industry/Entity Type

Marketing

Contact Information for Business Card

Velmora Health Care Marketing
Dana Prewitt- CEO
#(407)555-0172
email-dana@velmora.com
website- velmora.com

Font styles to use
Sans Serif

Colors
ec1f27
f37122
ffc214
fbed22
fbf289
f04a50

Requirements
Must have
• The logo and required information
Nice to have
• icons by the information
Should not have
• child like font

```html
<!DOCTYPE html>
<html lang="en">
<head>
<meta charset="UTF-8">
<title>Velmora Health Care Marketing — Business Card</title>
<link href="https://fonts.googleapis.com/css2?family=Raleway:wght@300&family=Open+Sans:wght@400;700;800&display=swap" rel="stylesheet">
<style>
  :root{
    --stage:#363636;
    --paper:#ffffff;
    --brand-red:#b3242a;
    --deep-red:#a01f22;
    --flame-orange:#f37122;
    --flame-gold:#f7941e;
    --ink-grey:#555555;
    --soft-grey:#9a9a9a;
    --mark-tint:#f6e4dc;
  }
  *{box-sizing:border-box;margin:0;padding:0}
  html,body{width:1200px;height:950px;overflow:hidden}
  body{background:var(--stage);position:relative;font-family:"Open Sans",Arial,sans-serif}

  .card{
    position:absolute;left:280px;width:640px;height:370px;border-radius:24px;overflow:hidden;
    box-shadow:0 14px 30px rgba(0,0,0,.45);
  }
  .card--front{top:70px;background:var(--paper)}
  .card--back{top:500px;background:radial-gradient(ellipse at 50% 45%,var(--flame-gold) 0%,var(--flame-orange) 40%,#d4461f 70%,var(--deep-red) 100%)}

  /* front */
  .brand-mark-area{position:absolute;right:-30px;top:-40px;width:330px;height:210px;border-radius:50%;
    background:radial-gradient(ellipse at center,var(--mark-tint) 0%,rgba(246,228,220,0) 70%)}
  .brand{position:absolute;left:48px;top:70px}
  .brand__row{display:flex;align-items:center;gap:12px}
  .brand__dot{width:34px;height:34px;border-radius:50%;background:var(--flame-orange)}
  .brand__name{font-family:"Raleway",Arial,sans-serif;font-weight:300;font-size:40px;letter-spacing:4px;color:var(--brand-red);line-height:1}
  .brand__tagline{font-family:"Raleway",Arial,sans-serif;font-weight:300;font-size:11.5px;letter-spacing:2.4px;color:var(--brand-red);
    margin-top:8px;padding-top:6px;border-top:1px solid #d9b0a8;display:inline-block}

  .person{position:absolute;left:48px;top:218px}
  .person__name{font-weight:800;font-size:26px;color:var(--brand-red);letter-spacing:.5px}
  .person__role{font-weight:700;font-size:16px;color:var(--flame-gold);margin-top:2px}

  .contact{position:absolute;right:48px;top:150px;list-style:none}
  .contact__item{display:flex;align-items:center;gap:9px;font-size:14px;color:var(--ink-grey);margin-bottom:9px}
  .contact__icon{width:20px;height:20px;border-radius:50%;background:var(--brand-red);display:flex;align-items:center;justify-content:center}
  .contact__icon svg{width:11px;height:11px}

  .corner-tab{position:absolute;left:-10px;bottom:-10px;width:60px;height:30px;border-radius:10px;background:var(--brand-red)}

  /* back */
  .back-brand{position:absolute;left:0;right:0;top:120px;text-align:center;color:#fff}
  .back-brand__row{display:inline-flex;align-items:center;gap:16px}
  .back-brand__dot{width:44px;height:44px;border-radius:50%;background:#fff;opacity:.9}
  .back-brand__name{font-family:"Raleway",Arial,sans-serif;font-weight:300;font-size:64px;letter-spacing:7px;line-height:1}
  .back-brand__tagline{font-family:"Raleway",Arial,sans-serif;font-weight:300;font-size:16px;letter-spacing:3.5px;
    display:inline-block;margin-top:12px;padding-top:8px;border-top:1px solid rgba(255,255,255,.8)}
</style>
</head>
<body>

<section class="card card--front">
  <div class="brand-mark-area" role="img" aria-label="Faint brand mark decoration"></div>

  <div class="brand">
    <div class="brand__row">
      <span class="brand__dot"></span>
      <span class="brand__name">VELMORA</span>
    </div>
    <div class="brand__tagline">HEALTH CARE MARKETING</div>
  </div>

  <div class="person">
    <div class="person__name">DANA PREWITT</div>
    <div class="person__role">CEO</div>
  </div>

  <ul class="contact">
    <li class="contact__item">
      <span class="contact__icon"><svg viewBox="0 0 24 24"><path fill="#fff" d="M6.6 10.8a15 15 0 0 0 6.6 6.6l2.2-2.2c.3-.3.7-.4 1-.2 1.1.4 2.3.6 3.6.6.6 0 1 .4 1 1V20c0 .6-.4 1-1 1A17 17 0 0 1 3 4c0-.6.4-1 1-1h3.5c.6 0 1 .4 1 1 0 1.3.2 2.5.6 3.6.1.3 0 .7-.2 1z"/></svg></span>
      (407)555-0172
    </li>
    <li class="contact__item">
      <span class="contact__icon"><svg viewBox="0 0 24 24"><path fill="#fff" d="M2 5h20v14H2z"/><path fill="none" stroke="#b3242a" stroke-width="2" d="M2 5l10 8 10-8"/></svg></span>
      dana@velmora.com
    </li>
    <li class="contact__item">
      <span class="contact__icon"><svg viewBox="0 0 24 24"><g fill="none" stroke="#fff" stroke-width="2"><circle cx="12" cy="12" r="9"/><path d="M3 12h18M12 3c3 3 3 15 0 18M12 3c-3 3-3 15 0 18"/></g></svg></span>
      www.velmora.com
    </li>
  </ul>

  <span class="corner-tab"></span>
</section>

<section class="card card--back">
  <div class="back-brand">
    <div class="back-brand__row">
      <span class="back-brand__dot"></span>
      <span class="back-brand__name">VELMORA</span>
    </div>
    <br>
    <div class="back-brand__tagline">HEALTH CARE MARKETING</div>
  </div>
</section>

</body>
</html>
```